Logo on the left corner with slogan written in italics: When care matters most.
Contact us
Telephone number to be provided.
Physical Address to be provided.
Email to be provided.
Picture of nature at the background with pictures with caring hands, disabled individuals under our care.
Home page
Brightfield Support Services Australia is a registered QCPA service provider in NSW. It provides care and support to individuals with disability together with their families.
VISION
To be the number one choice QCPA provider for services that empower individuals with disability discover their greatest potentials.
MISSION STATEMENT
Brightfield Support Services Australia is determined to improve the lives of participants by providing highest quality of care and services that empower individuals with disability participate in all aspects of community life.
VALUES
At Brightfield Support Services Australia we are committed to:
RESPECT
Working with services users in a professional and respectful manner as we take cognoscente of their rights to exercise control over their own lives according to their own values and preferences.
INTEGRITY
Delivering care and support to our participants in an ethical and trustworthy manner.
CARE
Working constructively and collaboratively with families and carers in providing support and care to participants while treating them as individuals by providing tailored services to meet their needs.
EMPOWERMENT
Empowering individuals make positive life choices through inclusion and recognising diversity.
WHAT WE DO
Brightfield support Services Australia is authorised by QCPA to provide wide range of care and support to participants with disability in the following care groups:
1. Assistance in coordinating or managing life stages, transitions and supports.
2. Assistance with daily life tasks in a group of shared living arrangement.
3. Assistance in daily living and life skills.
4. Assistance with daily personal activities.
5. Participation in community, social and civic activities.
Request to you Artforge: Will you be able to create a business email address for us?
Coding
Coded - Design and coding required
Number of Pages Required
5+ page
Colors
Designer to choose colors to be used in the design.
Look and feel
Each slider illustrates characteristics of the customer's brand and the style your logo design should communicate.

```html
<!DOCTYPE html>
<html lang="en">
<head>
<meta charset="utf-8">
<title>Brightfield Support Services Australia</title>
<link rel="stylesheet" href="https://fonts.googleapis.com/css2?family=Poppins:wght@400;500;600;700&family=Lora:ital@1&display=swap">
<style>
:root{
  --green:#63b246;
  --green-light:#8cc63f;
  --pink:#d9237f;
  --pink-light:#e8689f;
  --ink:#231f20;
  --text:#2b2b2b;
  --muted:#c9c9c9;
  --line:#cfcfcf;
  --white:#ffffff;
}
*{margin:0;padding:0;box-sizing:border-box}
html,body{width:977px;height:1200px;overflow:hidden;background:var(--white);font-family:'Poppins',sans-serif;color:var(--text)}
.page{position:relative;width:977px;height:1200px}
.abs{position:absolute}

/* header */
.site-header{position:absolute;left:0;top:0;width:977px;height:81px;background:var(--white);z-index:3}
.slogan{font-family:'Lora',serif;font-style:italic;font-size:12px;color:var(--ink)}
.header-left{left:140px;top:30px;width:280px;text-align:center}
.header-left .slogan{padding-bottom:6px;border-bottom:1px solid var(--line)}
.main-nav{display:flex;justify-content:center;gap:10px;margin-top:5px;font-size:8px;color:var(--pink)}
.main-nav .sep{color:var(--pink)}
.header-right{left:557px;top:32px;width:278px;text-align:center;font-size:10px}
.header-right .call{padding-bottom:6px;border-bottom:1px solid var(--line)}
.header-right .call b{color:var(--green);font-weight:600}
.header-right .mail{margin-top:5px;font-size:8px;color:var(--pink)}
.header-right .mail span{color:var(--ink)}

/* logo */
.brand{left:428px;top:22px;width:120px;height:120px;z-index:4}
.brand-frame{position:absolute;left:0;top:0;width:120px;height:120px;background:var(--white);transform:rotate(45deg);border-radius:10px;box-shadow:0 2px 6px rgba(0,0,0,.15)}
.brand-name{position:absolute;left:0;top:0;width:120px;height:120px;display:flex;align-items:center;justify-content:center;text-align:center;font-size:10px;font-weight:600;line-height:1.25;color:var(--pink)}

/* hero */
.hero{left:0;top:81px;width:977px;height:353px;background:linear-gradient(100deg,#6f8a4a 0%,#9fb77a 40%,#c9cdb6 65%,#e6e2dc 80%,#7d8f5b 100%)}
.hero-copy{left:141px;top:184px;color:var(--white)}
.hero-title{font-size:27px;font-weight:600;line-height:1.12}
.hero-text{font-size:10.5px;margin-top:10px;line-height:1.45}
.btn{display:inline-block;border-radius:14px;background:var(--green);color:var(--white);font-size:8px;font-weight:600;text-align:center}
.hero .btn{position:absolute}
.hero-btn{left:141px;top:301px;width:81px;height:27px;line-height:27px}
.slider-dots{left:802px;top:229px;display:flex;flex-direction:column;gap:5px}
.slider-dots i{display:block;width:8px;height:8px;border:1px solid rgba(255,255,255,.9);border-radius:50%}
.slider-dots i.on{background:radial-gradient(circle,#fff 2px,transparent 2.5px)}

/* mission */
.mission{left:0;top:434px;width:977px;height:100px;background:var(--pink);overflow:hidden}
.mission-word{position:absolute;left:-40px;top:-40px;font-size:150px;font-weight:600;letter-spacing:2px;color:rgba(255,255,255,.14);white-space:nowrap;line-height:1}
.mission-text{position:absolute;left:230px;top:35px;width:516px;font-size:10.2px;line-height:1.5;text-align:justify;text-align-last:center;color:var(--ink)}

/* services */
.services{left:0;top:534px;width:977px;height:340px}
.bubble-text{font-size:10px;font-weight:600;text-anchor:middle}
.explore-btn{position:absolute;left:440px;top:885px;width:97px;height:27px;line-height:27px}

/* footer */
.site-footer{left:0;top:955px;width:977px;height:245px;background:var(--ink);color:var(--white)}
.site-footer .slogan{color:var(--white);position:absolute;left:141px;top:44px;font-size:11px}
.footer-map{left:142px;top:69px;width:82px;height:63px;background:#bdbdbd;border-radius:40% 30% 45% 35%}
.footer-contact{left:322px;top:45px;font-size:8px}
.footer-contact .row{display:flex;align-items:center;gap:7px;margin-bottom:5px}
.footer-contact .phone{font-size:10px;font-weight:600;letter-spacing:.5px}
.footer-contact .address{margin-top:22px;display:flex;gap:7px;line-height:1.65}
.footer-contact .contact-link{margin-top:20px;margin-left:16px}
.quick-links{left:499px;top:45px;font-size:8px}
.quick-links h3,.newsletter h3{font-size:10.5px;font-weight:500;margin-bottom:6px}
.quick-links li{list-style:none;line-height:16.3px}
.newsletter{left:678px;top:45px;width:158px;text-align:center}
.news-input{margin-top:4px;height:21px;border-radius:11px;background:var(--white);display:flex;align-items:center;justify-content:space-between;padding:0 4px 0 12px;font-size:7.5px;color:#9a9a9a}
.socials{display:flex;justify-content:center;gap:6px;margin-top:11px}
.socials i{display:block;width:9px;height:9px;border:1px solid var(--white);border-radius:2px}
.copyright{left:141px;top:217px;font-size:7px;color:#d8d8d8}
.footer-figures{left:806px;top:189px;width:62px;height:56px;background:linear-gradient(120deg,var(--green) 0%,var(--pink-light) 70%);border-radius:30px 30px 0 0;opacity:.9}
</style>
</head>
<body>
<div class="page">

  <header class="site-header">
    <div class="abs header-left">
      <p class="slogan">When care matters most.</p>
      <nav class="main-nav"><span>Home</span><span class="sep">•</span><span>About</span><span class="sep">•</span><span>What We Do</span><span class="sep">•</span><span>Contact</span></nav>
    </div>
    <div class="abs header-right">
      <p class="call">Call Us Today!. <b>800 . 555 . 0142</b></p>
      <p class="mail"><span>e.</span> hello@brightfieldsupport.example</p>
    </div>
  </header>

  <div class="abs brand">
    <div class="brand-frame"></div>
    <div class="brand-name">Brightfield<br>Support Services<br>Australia</div>
  </div>

  <section class="abs hero" role="img" aria-label="Photo of a smiling carer embracing an older woman in a wheelchair in a leafy park">
    <div class="abs hero-copy" style="top:103px;left:141px">
      <h1 class="hero-title">Brightfield Support<br>Services Australia</h1>
      <p class="hero-text">Provides care and support to individuals with disability<br>together with their families</p>
    </div>
    <a class="btn hero-btn" style="top:220px">About Us</a>
    <div class="abs slider-dots" style="top:148px"><i class="on"></i><i></i><i></i><i></i><i></i></div>
  </section>

  <section class="abs mission">
    <div class="mission-word">Our Mission</div>
    <p class="mission-text">Brightfield Support Services Australia is determined to improve the lives of service users by providing highest quality of care and services that empower individuals with disability participate in all aspects of community life.</p>
  </section>

  <section class="abs services">
    <svg width="977" height="340" viewBox="0 0 977 340">
      <defs>
        <linearGradient id="g-green" x1="0" y1="0" x2="1" y2="0"><stop offset="0" stop-color="#5aaf45"/><stop offset="1" stop-color="#8cc63f"/></linearGradient>
        <linearGradient id="g-pink" x1="0" y1="0" x2="1" y2="0"><stop offset="0" stop-color="#d9237f"/><stop offset="1" stop-color="#e96ea3"/></linearGradient>
        <filter id="soft" x="-20%" y="-20%" width="140%" height="160%"><feDropShadow dx="4" dy="8" stdDeviation="6" flood-opacity=".18"/></filter>
      </defs>
      <g stroke="#555" stroke-width="1">
        <line x1="236" y1="0" x2="236" y2="90"/><line x1="362" y1="0" x2="362" y2="172"/>
        <line x1="488" y1="0" x2="488" y2="90"/><line x1="615" y1="0" x2="615" y2="172"/>
        <line x1="741" y1="0" x2="741" y2="90"/>
      </g>
      <g filter="url(#soft)">
        <g fill="url(#g-green)">
          <ellipse cx="236" cy="148" rx="95" ry="66"/><path d="M185 196 Q173 222 171 240 Q190 215 218 208 Z"/>
          <ellipse cx="488" cy="148" rx="95" ry="66"/><path d="M520 200 Q545 218 556 245 Q557 214 548 196 Z"/>
          <ellipse cx="741" cy="148" rx="95" ry="66"/><path d="M776 200 Q800 222 806 242 Q812 214 804 192 Z"/>
        </g>
        <g fill="url(#g-pink)">
          <ellipse cx="362" cy="231" rx="95" ry="66"/><path d="M396 283 Q420 300 428 325 Q432 298 424 276 Z"/>
          <ellipse cx="615" cy="231" rx="95" ry="66"/><path d="M650 283 Q675 300 681 325 Q686 298 678 276 Z"/>
        </g>
      </g>
      <g fill="#fff">
        <circle cx="236" cy="97" r="6"/><circle cx="488" cy="97" r="6"/><circle cx="741" cy="97" r="6"/>
        <circle cx="362" cy="181" r="6"/><circle cx="615" cy="181" r="6"/>
      </g>
      <text class="bubble-text" fill="#1f1f1f"><tspan x="236" y="138">Assistance in coordinating</tspan><tspan x="236" y="152">or managing life stages, transi-</tspan><tspan x="236" y="166">tions &amp; supports.</tspan></text>
      <text class="bubble-text" fill="#1f1f1f"><tspan x="488" y="148">Assistance in daily living</tspan><tspan x="488" y="162">&amp; life skills.</tspan></text>
      <text class="bubble-text" fill="#1f1f1f"><tspan x="741" y="148">Participation in community,</tspan><tspan x="741" y="162">social &amp; civic activities.</tspan></text>
      <text class="bubble-text" fill="#fff"><tspan x="362" y="227">Assistance with daily life tasks</tspan><tspan x="362" y="241">in a group of shared living</tspan><tspan x="362" y="255">a rangement.</tspan></text>
      <text class="bubble-text" fill="#fff"><tspan x="615" y="233">Assistance with daily person-</tspan><tspan x="615" y="247">al activities.</tspan></text>
    </svg>
  </section>
  <a class="btn explore-btn">Explore More</a>

  <footer class="abs site-footer">
    <p class="slogan">When care matters most.</p>
    <div class="abs footer-map" role="img" aria-label="Illustration of caring hands over a map of Australia"></div>
    <div class="abs footer-contact">
      <div class="row phone">
        <svg width="9" height="9" viewBox="0 0 10 10"><path d="M2 1 L4 3 L3 4 Q4 6 6 7 L7 6 L9 8 L8 9 Q3 9 1 2 Z" fill="none" stroke="#fff" stroke-width=".8"/></svg>
        1 . 800 . 555 . 0142</div>
      <div class="row">
        <svg width="9" height="9" viewBox="0 0 10 10"><rect x="1" y="3" width="8" height="5.5" fill="none" stroke="#fff" stroke-width=".8"/><path d="M1 3 L5 6 L9 3" fill="none" stroke="#fff" stroke-width=".8"/></svg>
        hello@brightfieldsupport.example</div>
      <div class="address">
        <svg width="9" height="10" viewBox="0 0 10 11"><path d="M5 10 Q1 6 1 4 A4 4 0 0 1 9 4 Q9 6 5 10 Z" fill="none" stroke="#fff" stroke-width=".8"/><circle cx="5" cy="4" r="1.3" fill="#fff"/></svg>
        <span>Unit 4 Harbour Lane<br>Riverside Park<br>Northmead</span>
      </div>
      <p class="contact-link">Contact</p>
    </div>
    <div class="abs quick-links">
      <h3>Quick Link</h3>
      <ul><li>Home</li><li>ABout Us</li><li>What we do</li><li>Blog</li><li>Careers</li></ul>
    </div>
    <div class="abs newsletter">
      <h3>Sign Up Newsletter</h3>
      <div class="news-input"><span>Name@emial.com</span>
        <svg width="13" height="13" viewBox="0 0 14 14"><circle cx="7" cy="7" r="6" fill="none" stroke="#231f20" stroke-width="1"/><path d="M4 7 H10 M7.5 4.5 L10 7 L7.5 9.5" fill="none" stroke="#231f20" stroke-width="1"/></svg>
      </div>
      <div class="socials"><i></i><i></i><i></i><i></i></div>
    </div>
    <p class="abs copyright">© 2020 Brightfield Support Services Australia. All Rights Reserved.</p>
    <div class="abs footer-figures" role="img" aria-label="Illustration of a carer helping a person walk"></div>
  </footer>

</div>
</body>
</html>
```